Harbor Shell Interiors web design

We need to relaunch my commercial and retail interior design + construction company after being out of the industry's for 10 plus years.

```html
<!DOCTYPE html>
<html lang="en">
<head>
<meta charset="utf-8">
<title>Harbor Shell Interiors</title>
<link href="https://fonts.googleapis.com/css2?family=Montserrat:wght@400;500;600;700;800&display=swap" rel="stylesheet">
<style>
:root{
  --blue:#1a8cf0;
  --blue-dark:#0d6fd0;
  --navy:#111a2b;
  --ink:#1b1f27;
  --muted:#4a4f58;
  --pale:#eaf4fd;
  --grey:#eef0f3;
  --card-grey:#eceef1;
  --white:#ffffff;
  --bar:#121417;
}
*{box-sizing:border-box;margin:0;padding:0}
html,body{width:1200px;height:5262px;overflow:hidden}
body{font-family:"Montserrat",sans-serif;color:var(--ink);background:var(--white);position:relative}
section,header,footer{position:absolute;left:0;width:1200px}

/* top bar */
.topbar{top:0;height:58px;background:var(--bar);color:var(--white);font-size:11px}
.topbar .ico{position:absolute;top:14px;width:30px;height:30px;border-radius:50%;background:var(--white);display:flex;align-items:center;justify-content:center}
.topbar .txt{position:absolute;line-height:15px}
.social{position:absolute;top:14px;width:28px;height:28px;border-radius:50%;background:var(--blue)}

/* nav */
.nav{top:58px;height:86px;background:var(--white)}
.brand{position:absolute;left:125px;top:18px;display:flex;align-items:center;gap:10px}
.brand .mark{width:46px;height:46px;background:var(--blue)}
.brand .name{font-weight:800;font-size:15px;line-height:16px;color:var(--navy);letter-spacing:.5px;text-transform:uppercase}
.menu{position:absolute;top:30px;font-size:13px;font-weight:500;color:var(--ink)}
.menu.active{font-weight:700}
.menu.active::after{content:"";display:block;height:2px;background:var(--blue);margin-top:6px}
.btn-outline{position:absolute;border:2px solid var(--blue);color:var(--blue);font-size:12px;font-weight:600;display:flex;align-items:center;justify-content:center}

/* hero */
.hero{top:144px;height:582px;background:linear-gradient(160deg,#8d949a 0%,#4c5258 45%,#2c2f31 100%)}
.hero h1{position:absolute;left:0;width:1200px;top:132px;text-align:center;color:var(--white);font-size:44px;line-height:50px;font-weight:700;text-transform:uppercase}
.hero p{position:absolute;left:0;width:1200px;top:302px;text-align:center;color:var(--white);font-size:12px;line-height:15px}
.hero .btn{position:absolute;left:523px;top:367px;width:131px;height:41px;border:1px solid var(--white);color:var(--white);font-size:11px;font-weight:600;display:flex;align-items:center;justify-content:center}

/* about */
.about{top:726px;height:780px}
.about .frame{position:absolute;left:114px;top:98px;width:484px;height:522px;border:1px solid #c9ccd1;padding:10px}
.about .photo{width:100%;height:100%;background:linear-gradient(150deg,#d9dfe0,#f3f3f1 50%,#b8bcbd)}
.h2{font-weight:800;text-transform:uppercase;color:var(--navy);font-size:54px;line-height:62px}
.about .h2{position:absolute;left:628px;top:98px}
.about .copy{position:absolute;left:628px;width:450px;font-size:12.5px;line-height:21.5px;color:var(--muted)}
.btn-box{position:absolute;border:1px solid var(--ink);font-size:11px;font-weight:600;display:flex;align-items:center;justify-content:center;background:var(--white)}

/* services */
.services{top:1506px;height:718px;background:var(--pale)}
.services .h2{position:absolute;left:125px;top:90px}
.services .intro{position:absolute;left:125px;top:166px;width:420px;font-size:12.5px;line-height:16px;color:var(--ink)}
.services .thumb{position:absolute;left:658px;top:120px;width:204px;height:92px;background:linear-gradient(90deg,#8a6b4e,#d9c9b2 55%,#6f5a45)}
.counter{position:absolute;left:875px;top:132px;font-size:30px;font-weight:700;color:var(--navy)}
.counter-label{position:absolute;left:875px;top:180px;font-size:12px;font-weight:600;color:var(--navy)}
.card{position:absolute;top:283px;width:222px;height:239px;background:var(--white);text-align:center}
.card svg{position:absolute;left:91px;top:24px}
.card h3{position:absolute;left:0;top:78px;width:100%;font-size:18px;font-weight:700;color:var(--navy)}
.card p{position:absolute;top:114px;left:20px;right:20px;font-size:11.5px;line-height:16px;color:var(--muted)}
.card a{position:absolute;display:block;left:0;top:194px;width:100%;text-align:center;font-size:10px;font-weight:700;color:var(--blue);text-decoration:underline}
.circ{position:absolute;width:46px;height:46px;border-radius:50%;display:flex;align-items:center;justify-content:center}

/* why */
.why{top:2224px;height:764px}
.why .border{position:absolute;left:125px;top:94px;width:380px;height:576px;border:8px solid var(--blue)}
.why .photo{position:absolute;left:161px;top:129px;width:465px;height:509px;background:linear-gradient(170deg,#f1f0ee,#d8d2c8 55%,#5a554f)}
.why .h2{position:absolute;left:652px;top:92px}
.feat{position:absolute;left:652px;display:flex;align-items:center;gap:14px;font-size:20px;font-weight:600;color:var(--navy)}

/* experts */
.experts{top:2988px;height:554px;background:linear-gradient(120deg,#1a8cf0,#2d9bf5 50%,#1a86e8)}
.experts .h2{position:absolute;left:0;width:1200px;top:86px;text-align:center;color:var(--white)}
.team{position:absolute;top:190px;width:302px;height:266px}
.team .arrow{position:absolute;left:137px;top:112px}
.team span{position:absolute;left:0;width:100%;bottom:34px;text-align:center;color:var(--white);font-size:19px;font-weight:700;text-transform:uppercase;line-height:24px}

/* testimonials */
.reviews{top:3542px;height:724px}
.reviews h2{position:absolute;left:125px;top:96px;font-size:44px;line-height:52px;font-weight:700;color:var(--navy)}
.nav-sq{position:absolute;top:102px;width:63px;height:62px;display:flex;align-items:center;justify-content:center}
.review{position:absolute;top:256px;width:298px;height:276px;background:var(--card-grey)}
.review.first{background:var(--white);box-shadow:0 6px 22px rgba(0,0,0,.08)}
.review .av{position:absolute;left:27px;top:45px;width:44px;height:44px;border-radius:50%;background:#9aa3ad}
.review .who{position:absolute;left:110px;top:48px;font-size:15px;font-weight:500;color:var(--navy)}
.review .role{position:absolute;left:110px;top:74px;font-size:10px;color:var(--blue)}
.review p{position:absolute;left:24px;right:24px;top:120px;font-size:11.5px;line-height:26px;color:var(--ink)}

/* contact */
.contact{top:4266px;height:507px;background:var(--grey)}
.contact .map{position:absolute;left:0;top:0;width:589px;height:507px;background:linear-gradient(135deg,#e8ecef,#dfe7ee 50%,#c9d9ef)}
.contact h2{position:absolute;left:640px;top:52px;font-size:44px;font-weight:800;color:var(--navy);text-transform:uppercase}
.field{position:absolute;background:#f5f6f8;font-size:10px;color:#555;padding:12px 10px}
.submit{position:absolute;left:640px;top:403px;width:433px;height:43px;background:var(--blue);color:var(--white);font-size:11px;font-weight:600;display:flex;align-items:center;justify-content:center}

/* footer */
.footer{top:4773px;height:429px;background:var(--white)}
.footer .brand{top:82px}
.footer h4{position:absolute;font-size:20px;font-weight:700;color:var(--navy);text-transform:uppercase;line-height:24px}
.footer .about-txt{position:absolute;left:125px;top:235px;width:340px;font-size:12px;line-height:20.5px;color:var(--muted)}
.footer ul{position:absolute;left:560px;top:210px;list-style:none;font-size:12px;line-height:22px;color:var(--ink)}
.subscribe-title{position:absolute;left:791px;top:192px;font-size:17px;font-weight:600;color:var(--navy)}
.subscribe{position:absolute;left:791px;top:231px;width:252px;height:45px;background:var(--card-grey);font-size:10px;padding:16px 22px;color:#444}
.subscribe-btn{position:absolute;left:1043px;top:231px;width:57px;height:45px;background:var(--blue);display:flex;align-items:center;justify-content:center}
.copyright{position:absolute;left:0;top:5202px;width:1200px;height:60px;background:var(--bar);color:var(--white);font-size:13px;display:flex;align-items:center;justify-content:center}
.copyright b{font-weight:700;margin:0 4px}
</style>
</head>
<body>

<header class="topbar">
  <div class="ico" style="left:124px"><svg width="12" height="14" viewBox="0 0 12 14"><path d="M6 0a5 5 0 0 0-5 5c0 4 5 9 5 9s5-5 5-9a5 5 0 0 0-5-5zm0 7a2 2 0 1 1 0-4 2 2 0 0 1 0 4z" fill="#1a8cf0"/></svg></div>
  <div class="txt" style="left:170px;top:14px">Address Level 4, 18 Quay Lane<br>Portview VIC 3100</div>
  <div class="ico" style="left:386px"><svg width="13" height="13" viewBox="0 0 24 24"><path d="M6.6 10.8a15 15 0 0 0 6.6 6.6l2.2-2.2a1 1 0 0 1 1-.25 11.4 11.4 0 0 0 3.6.57 1 1 0 0 1 1 1V20a1 1 0 0 1-1 1A17 17 0 0 1 3 4a1 1 0 0 1 1-1h3.5a1 1 0 0 1 1 1c0 1.25.2 2.45.57 3.57a1 1 0 0 1-.25 1z" fill="#1a8cf0"/></svg></div>
  <div class="txt" style="left:431px;top:22px">03 5550 0142</div>
  <div class="txt" style="left:832px;top:22px">Follow Us On:</div>
  <span class="social" style="left:920px"></span>
  <span class="social" style="left:961px"></span>
  <span class="social" style="left:1002px"></span>
  <span class="social" style="left:1045px"></span>
</header>

<header class="nav">
  <div class="brand"><span class="mark"></span><span class="name">Harbor Shell<br>Interiors</span></div>
  <span class="menu active" style="left:405px">Home</span>
  <span class="menu" style="left:506px">About Us</span>
  <span class="menu" style="left:630px">Services</span>
  <span class="menu" style="left:748px">Project</span>
  <span class="menu" style="left:857px">Blogs</span>
  <span class="btn-outline" style="left:940px;top:24px;width:131px;height:41px">Contact Us</span>
</header>

<section class="hero" role="img" aria-label="Photo of a modern commercial building with wide stone steps">
  <h1>Have you experienced<br>frustration in the design<br>and building process?</h1>
  <p>approach to guarantee superior outcomes for your upcoming<br>commercial and retail interior fitouts?</p>
  <span class="btn">Our Services</span>
</section>

<section class="about">
  <div class="frame"><div class="photo" role="img" aria-label="Photo of architectural plans with a pen and a house model on a desk"></div></div>
  <h2 class="h2">About Us</h2>
  <p class="copy" style="top:178px">At Harbor Shell Interiors, we were founded with your needs at the forefront—a dedication to delivering a transformative leap in results for your commercial and retail projects. Our pride lies in surpassing client expectations, achieved through meticulous planning and proactive problem-solving before challenges even surface.</p>
  <p class="copy" style="top:334px">Guided by the expertise of interior designer and commercial builder, Mr. Daniel Rowe since 1994, our dedicated team seamlessly manages every facet of your project. From meticulous design and innovative design to thorough documentation, efficient project management, expert construction, and thorough maintenance, we bring precision, purpose, value, and passion to every stage. Our commitment ensures that your high-end commercial and retail fitouts are not just met but exceeded—delivering on time, on budget, and hassle-free."</p>
  <span class="btn-box" style="left:628px;top:562px;width:131px;height:41px;color:var(--blue);border-color:var(--blue)">Learn More</span>
</section>

<section class="services">
  <h2 class="h2">Our Services</h2>
  <p class="intro">If you're searching for a superior way to design and construct your next project, contact us to arrange an obligation-free consultation. Experience the Harbor Shell Interiors difference—where excellence meets innovation!</p>
  <div class="thumb" role="img" aria-label="Photo of a furnished living room interior"></div>
  <div class="counter">4,27,223</div>
  <div class="counter-label">Project Have Been Completed</div>

  <div class="card" style="left:125px">
    <svg width="40" height="40" viewBox="0 0 40 40" fill="none" stroke="#1a8cf0" stroke-width="2"><circle cx="17" cy="17" r="11"/><path d="M25 25l10 10"/><path d="M12 17h10M17 12v10"/></svg>
    <h3>Site Inspection</h3><p>Pre-lease site inspections and advice on base building works</p><a>READ MORE</a>
  </div>
  <div class="card" style="left:368px">
    <svg width="40" height="40" viewBox="0 0 40 40" fill="none" stroke="#1a8cf0" stroke-width="2"><circle cx="22" cy="18" r="12"/><path d="M22 11v14M18 14h6a2 2 0 0 1 0 4h-4a2 2 0 0 0 0 4h6"/><path d="M4 30h10l6 4h14"/></svg>
    <h3>Budgeting</h3><p>Expert advice on construction budgets and required services</p><a>READ MORE</a>
  </div>
  <div class="card" style="left:609px">
    <svg width="40" height="40" viewBox="0 0 40 40" fill="none" stroke="#1a8cf0" stroke-width="2"><rect x="7" y="5" width="24" height="30" rx="2"/><path d="M12 13l2 2 4-4M12 21l2 2 4-4M12 29l2 2 4-4M21 13h6M21 21h6M21 29h6"/></svg>
    <h3>Planning Services</h3><p>Comprehensive planning from start to finish</p><a>READ MORE</a>
  </div>
  <div class="card" style="left:852px">
    <svg width="40" height="40" viewBox="0 0 40 40" fill="none" stroke="#1a8cf0" stroke-width="2"><rect x="5" y="14" width="24" height="20"/><path d="M10 20h6M10 26h14"/><circle cx="29" cy="12" r="8"/><path d="M25 12l3 3 5-5"/></svg>
    <h3>Design Approval</h3><p>Submission and approval processes for design fitouts in shopping centers</p><a>READ MORE</a>
  </div>

  <span class="circ" style="left:125px;top:572px;border:1px solid var(--ink);background:var(--white)"><svg width="12" height="14" viewBox="0 0 12 14"><path d="M9 1L3 7l6 6" stroke="#111" stroke-width="2.5" fill="none"/></svg></span>
  <span class="circ" style="left:194px;top:572px;background:var(--blue)"><svg width="12" height="14" viewBox="0 0 12 14"><path d="M3 1l6 6-6 6" stroke="#fff" stroke-width="2.5" fill="none"/></svg></span>
</section>

<section class="why">
  <div class="border"></div>
  <div class="photo" role="img" aria-label="Photo of a bright modern lounge interior with a white sofa"></div>
  <h2 class="h2">Why Choose<br>Us</h2>
  <div class="feat" style="top:246px"><svg width="40" height="34" viewBox="0 0 40 34" fill="none" stroke="#1a8cf0" stroke-width="1.8"><circle cx="12" cy="17" r="7"/><circle cx="28" cy="17" r="5"/><path d="M2 17h3M19 17h4M33 17h5M12 6v4M12 24v4"/></svg>Holistic Approach</div>
  <div class="feat" style="top:342px"><svg width="40" height="34" viewBox="0 0 40 34" fill="none" stroke="#1a8cf0" stroke-width="1.8"><rect x="4" y="6" width="14" height="26"/><rect x="22" y="14" width="14" height="18"/><path d="M8 11h6M8 17h6M8 23h6M26 19h6M26 25h6"/></svg>Specialisations</div>
  <div class="feat" style="top:440px"><svg width="40" height="34" viewBox="0 0 40 34" fill="none" stroke="#1a8cf0" stroke-width="1.8"><circle cx="20" cy="15" r="11"/><path d="M14 14h12M14 18h8M6 31h28"/></svg>Peace Of Mind</div>
  <div class="feat" style="top:538px"><svg width="40" height="34" viewBox="0 0 40 34" fill="none" stroke="#1a8cf0" stroke-width="1.8"><rect x="6" y="4" width="14" height="28"/><rect x="22" y="12" width="12" height="20"/><path d="M10 9h6M10 15h6M10 21h6M26 17h4M26 23h4"/></svg>Compliance</div>
  <span class="btn-box" style="left:654px;top:617px;width:131px;height:39px">Learn More</span>
</section>

<section class="experts">
  <h2 class="h2">Our Expert Teams</h2>
  <div class="team" style="left:125px;background:linear-gradient(160deg,#3a4d6a,#1c2534)" role="img" aria-label="Photo of a consulting team meeting at a table">
    <svg class="arrow" width="28" height="28" viewBox="0 0 28 28"><path d="M6 22L22 6M10 6h12v12" stroke="#fff" stroke-width="2" fill="none"/></svg>
    <span>Consulting Team</span>
  </div>
  <div class="team" style="left:448px;background:linear-gradient(160deg,#7c6a4d,#34302a)" role="img" aria-label="Photo of a construction team on site in safety gear">
    <svg class="arrow" width="28" height="28" viewBox="0 0 28 28"><path d="M6 22L22 6M10 6h12v12" stroke="#fff" stroke-width="2" fill="none"/></svg>
    <span>Construction Team</span>
  </div>
  <div class="team" style="left:771px;background:linear-gradient(160deg,#5d6b7c,#2a3340)" role="img" aria-label="Photo of finance advisers in an office">
    <svg class="arrow" width="28" height="28" viewBox="0 0 28 28"><path d="M6 22L22 6M10 6h12v12" stroke="#fff" stroke-width="2" fill="none"/></svg>
    <span>Finance and Leagal<br>Consulting</span>
  </div>
</section>

<section class="reviews">
  <h2>What People Say About<br>Us</h2>
  <span class="nav-sq" style="left:946px;background:#e3ecf8"><svg width="14" height="18" viewBox="0 0 14 18"><path d="M11 2L4 9l7 7" stroke="#1a8cf0" stroke-width="3" fill="none"/></svg></span>
  <span class="nav-sq" style="left:1010px;background:var(--blue)"><svg width="14" height="18" viewBox="0 0 14 18"><path d="M3 2l7 7-7 7" stroke="#fff" stroke-width="3" fill="none"/></svg></span>

  <div class="review first" style="left:125px">
    <span class="av" role="img" aria-label="Client portrait"></span>
    <span class="who">Lena Marsh</span><span class="role">Trustworthy Owner</span>
    <p>"Lorem Ipsum is simply dummy text of the printing and typesetting industry. Lorem Ipsum has been the industry's standard dummy text ever since the 1500s, when an unknown printer."</p>
  </div>
  <div class="review" style="left:450px">
    <span class="av" role="img" aria-label="Client portrait"></span>
    <span class="who">Owen Hale</span><span class="role">Trustworthy Owner</span>
    <p>"Lorem Ipsum is simply dummy text of the printing and typesetting industry. Lorem Ipsum has been the industry's standard dummy text ever since the 1500s, when an unknown printer."</p>
  </div>
  <div class="review" style="left:775px">
    <span class="av" role="img" aria-label="Client portrait"></span>
    <span class="who">Priya Nolan</span><span class="role">Trustworthy Owner</span>
    <p>"Lorem Ipsum is simply dummy text of the printing and typesetting industry. Lorem Ipsum has been the industry's standard dummy text ever since the 1500s, when an unknown printer."</p>
  </div>
  <span class="btn-box" style="left:127px;top:587px;width:131px;height:39px">See All</span>
</section>

<section class="contact">
  <div class="map" role="img" aria-label="Street map showing the office location"></div>
  <h2>Get In Touch</h2>
  <div class="field" style="left:640px;top:145px;width:210px;height:39px">First Name:</div>
  <div class="field" style="left:858px;top:145px;width:215px;height:39px">Last Name:</div>
  <div class="field" style="left:640px;top:200px;width:210px;height:41px">Phone:</div>
  <div class="field" style="left:858px;top:200px;width:215px;height:41px">Email:</div>
  <div class="field" style="left:640px;top:255px;width:433px;height:129px">Massage</div>
  <span class="submit">Submit</span>
</section>

<footer class="footer">
  <div class="brand"><span class="mark"></span><span class="name">Harbor Shell<br>Interiors</span></div>
  <h4 style="left:125px;top:172px">About Harbor Shell<br>Interiors</h4>
  <p class="about-txt">At Harbor Shell Interiors, we were founded with your needs at the forefront—a dedication to delivering a transformative leap in results for your commercial and retail projects. Our pride lies in surpassing client expectations, achieved through meticulous planning and proactive problem-solving before challenges even surfac</p>
  <h4 style="left:558px;top:162px">Quick Links</h4>
  <ul><li>HOME</li><li>ABOUT US</li><li>SERVICES</li><li>BLOGS</li><li>CONTACT US</li></ul>
  <span class="subscribe-title">Subscribe Our Newsletter</span>
  <div class="subscribe">Email</div>
  <span class="subscribe-btn"><svg width="22" height="20" viewBox="0 0 22 20"><path d="M1 9L21 1l-6 18-4-7z" fill="#fff"/></svg></span>
</footer>

<div class="copyright">© Copyright 2023 <b>ABOUT Harbor Shell Interiors .</b> All Rights Reserved</div>

</body>
</html>
```